Product Designer Business Card

Small product design, engineering and prototyping firm in need of a clean, professional business card design. To support our 3D design and drawing services, we offer 3D printing, molding, and casting of plastics, silicones, resins, etc. Our logo can still be modified/changed if necessary. The red/orange color is preferred, but may be substituted with blue or green, potentially. Either way, the colour of the logo should be match/compliment colors used throughout the design. One thought is to have the logo/contact info on one side, with the other side describing services offered, like with a small icon of 3D printer, molding, casting, and computer with a 3D model on-screen.
Industry/Entity Type
Mechanical Engineering
Contact Information for Business Card
Company: Halvick Design
Phone: 613-582-4179
Email: myles@halvickdesign.ca

```html
<!DOCTYPE html>
<html lang="en">
<head>
<meta charset="utf-8">
<title>Halvick Design – Business Card</title>
<link rel="stylesheet" href="https://fonts.googleapis.com/css2?family=Exo+2:wght@400;600;700&display=swap">
<style>
  :root {
    --page-bg: #e9e6e4;
    --red-deep: #731404;
    --red-bright: #e3290c;
    --edge-dark: #4a0a04;
    --card-white: #ffffff;
    --card-mist: #eeeaea;
    --brand-ink: #5c0e07;
    --text-light: #ffffff;
  }
  * { margin: 0; padding: 0; box-sizing: border-box; }
  html, body {
    width: 1200px; height: 900px; overflow: hidden;
    background: var(--page-bg);
    font-family: "Exo 2", "Helvetica Neue", Arial, sans-serif;
  }
  .card {
    position: absolute; left: 112px; top: 147px;
    width: 975px; height: 605px;
    background: linear-gradient(180deg, var(--red-deep) 0%, #a81d07 45%, var(--red-bright) 100%);
    box-shadow: 0 18px 40px rgba(0,0,0,.18);
    overflow: hidden;
  }
  .card-shape { position: absolute; inset: 0; width: 975px; height: 605px; }
  .contact-block { position: absolute; left: 48px; top: 58px; color: var(--text-light); }
  .person-name { font-size: 39px; font-weight: 700; line-height: 1.1; }
  .person-title { font-size: 27px; font-weight: 400; margin-top: 2px; }
  .contact-list { list-style: none; margin-top: 26px; }
  .contact-list li {
    display: flex; align-items: center; gap: 10px;
    font-size: 26px; line-height: 35px;
  }
  .contact-list svg { width: 28px; height: 28px; flex: none; }
  .service-grid {
    position: absolute; left: 40px; top: 302px;
    display: grid; grid-template-columns: 130px 130px; column-gap: 30px; row-gap: 14px;
  }
  .service { display: flex; flex-direction: column; align-items: center; color: var(--text-light); }
  .service svg { width: 93px; height: 93px; }
  .service-label { font-size: 23px; margin-top: 4px; }
  .brand {
    position: absolute; left: 500px; top: 200px; width: 430px;
    text-align: center; color: var(--brand-ink);
    font-size: 62px; font-weight: 600; line-height: 1.15; letter-spacing: 4px;
  }
</style>
</head>
<body>
  <div class="card">
    <svg class="card-shape" viewBox="0 0 975 605" aria-hidden="true">
      <defs>
        <linearGradient id="mist" x1="0" y1="0" x2="1" y2="0">
          <stop offset="0" stop-color="var(--card-mist)"/>
          <stop offset="0.5" stop-color="var(--card-white)"/>
          <stop offset="1" stop-color="var(--card-mist)"/>
        </linearGradient>
      </defs>
      <path d="M 790 0 C 560 30 392 190 416 330 C 440 470 610 580 745 605 L 757 605 C 625 578 452 470 432 330 C 410 195 575 35 815 0 Z" fill="var(--edge-dark)"/>
      <path d="M 815 0 C 575 35 410 195 432 330 C 452 470 625 578 757 605 L 975 605 L 975 0 Z" fill="url(#mist)"/>
    </svg>

    <div class="contact-block">
      <div class="person-name">Elliot Warren</div>
      <div class="person-title">Managing Director</div>
      <ul class="contact-list">
        <li>
          <svg viewBox="0 0 28 28"><rect x="2" y="2" width="24" height="24" rx="5" fill="none" stroke="#fff" stroke-width="2.4"/><path d="M9 7 l3 0 l1.5 4 l-2 1.5 c1 2 2.5 3.5 4.5 4.5 l1.5 -2 l4 1.5 l0 3 c-7 1 -13 -5 -12.5 -12.5 z" fill="#fff"/></svg>
          613-582-4179
        </li>
        <li>
          <svg viewBox="0 0 28 28"><rect x="3" y="7" width="22" height="15" fill="#fff"/><path d="M3 7 l11 9 l11 -9" fill="none" stroke="#a81d07" stroke-width="1.8"/></svg>
          myles@halvickdesign.ca
        </li>
        <li>
          <svg viewBox="0 0 28 28" fill="none" stroke="#fff" stroke-width="2"><circle cx="14" cy="14" r="11"/><ellipse cx="14" cy="14" rx="5" ry="11"/><path d="M3 14 h22 M5 8.5 h18 M5 19.5 h18"/></svg>
          www.halvickdesign.ca
        </li>
      </ul>
    </div>

    <div class="service-grid">
      <div class="service">
        <svg viewBox="0 0 93 93" fill="none" stroke="#fff" stroke-width="3"><rect x="3" y="3" width="87" height="87" rx="10"/><rect x="22" y="22" width="49" height="48"/><path d="M22 32 h49 M38 32 v12 h16 v-12 M30 62 h33"/></svg>
        <span class="service-label">3D Printer</span>
      </div>
      <div class="service">
        <svg viewBox="0 0 93 93" fill="none" stroke="#fff" stroke-width="3"><rect x="3" y="3" width="87" height="87" rx="10"/><rect x="32" y="18" width="29" height="12"/><path d="M46 30 v10"/><rect x="26" y="40" width="41" height="10"/><rect x="24" y="56" width="45" height="18"/></svg>
        <span class="service-label">Molding</span>
      </div>
      <div class="service">
        <svg viewBox="0 0 93 93" fill="none" stroke="#fff" stroke-width="3"><rect x="3" y="3" width="87" height="87" rx="10"/><path d="M22 20 v30 h20 l6 -14 M22 50 l8 8"/><rect x="48" y="58" width="26" height="16"/><path d="M54 46 v10"/></svg>
        <span class="service-label">Casting</span>
      </div>
      <div class="service">
        <svg viewBox="0 0 93 93" fill="none" stroke="#fff" stroke-width="3"><rect x="3" y="3" width="87" height="87" rx="10"/><rect x="18" y="20" width="57" height="40" rx="2"/><path d="M40 60 v8 h13 v-8 M34 70 h25"/><path d="M46 30 l9 5 v10 l-9 5 l-9 -5 v-10 z M37 35 l9 5 l9 -5 M46 40 v10"/></svg>
        <span class="service-label">3d Model</span>
      </div>
    </div>

    <div class="brand">Halvick<br>Design</div>
  </div>
</body>
</html>
```